Brightfold websites redesign

Www.bright-fold.com needs to be redesigned along with updations. The incremental material will be provided for the updations. We are looking for complete redesign of the pages with the new content. The complete write up will be provided soon

Target Market(s)

Global

Coding

Coded - Design and coding required

Number of Pages Required

5+ page

Requirements
Must have
• A clean and slick design for the Consulting.
Should not have
• Too many pictures which reduces the speed of the site

```html
<!DOCTYPE html>
<html lang="en">
<head>
<meta charset="utf-8">
<title>Brightfold Consultancy</title>
<link href="https://fonts.googleapis.com/css2?family=Open+Sans:wght@400;600;700&family=Questrial&family=Play:wght@700&display=swap" rel="stylesheet">
<style>
:root{
  --maroon:#5e2121;
  --navy:#2e3f66;
  --navy-band:rgba(38,55,90,0.88);
  --sky:#3a9ac9;
  --grey-bg:#e6e6e6;
  --top-bg:#efefef;
  --text:#555;
  --white:#fff;
}
*{margin:0;padding:0;box-sizing:border-box}
html,body{width:729px;height:1200px;overflow:hidden;background:var(--white)}
body{position:relative;font-family:'Open Sans',sans-serif;color:var(--text)}
.abs{position:absolute}
.topbar{left:0;top:0;width:729px;height:90px;background:var(--top-bg)}
.contact-line{top:27px;font-size:10px;color:#666}
.contact-line span{color:var(--sky)}
.brand{left:278px;top:18px;display:flex;align-items:center;gap:7px}
.brand-dot{width:26px;height:26px;border-radius:50%;background:var(--navy)}
.brand-name{font-family:'Open Sans',sans-serif;font-size:22px;font-weight:400;color:var(--navy)}
.main-nav{left:28px;top:64px;width:671px;height:54px;background:var(--maroon);border-radius:4px;z-index:2}
.main-nav ul{list-style:none;display:flex;height:100%;align-items:center;justify-content:space-around;padding:0 30px}
.main-nav li{color:var(--white);font-size:9px;font-weight:700;letter-spacing:.3px}
.hero{left:0;top:90px;width:729px;height:358px;background:linear-gradient(110deg,#d5d7db 0%,#6b6f78 35%,#3d3f45 60%,#2a2b30 100%)}
.hero-shade{left:0;top:0;width:100%;height:100%;background:rgba(20,20,25,.35)}
.hero-title{left:0;top:90px;width:729px;text-align:center;font-family:'Questrial',sans-serif;font-size:44px;line-height:43px;color:var(--white)}
.hero-text{left:100px;top:188px;width:529px;text-align:center;font-size:8.5px;line-height:14px;color:var(--white)}
.btn{display:block;font-size:7px;color:var(--white);text-align:center;border-radius:3px}
.hero-btn{left:323px;top:233px;width:82px;height:25px;line-height:23px;border:1px solid #ccd;background:var(--navy)}
.slider-arrows{left:348px;top:340px;width:39px;height:18px;background:#eee}
.welcome{left:0;top:448px;width:729px;height:177px;background:var(--grey-bg)}
.sec-head{display:flex;justify-content:center;align-items:center;gap:8px;width:729px;left:0;font-family:'Play',sans-serif;font-size:20px;font-weight:700}
.sec-dot{width:15px;height:15px;border-radius:50%;background:var(--navy)}
.c-navy{color:var(--navy)}.c-maroon{color:var(--maroon)}
.welcome-text{left:80px;top:70px;width:569px;text-align:center;font-size:7px;line-height:14px;color:#666}
.welcome-btn{left:325px;top:124px;width:79px;height:24px;line-height:24px;background:var(--navy)}
.testimonials{left:0;top:956px;width:729px;height:202px;background:var(--maroon)}
.avatar{left:125px;top:84px;width:50px;height:50px;border-radius:50%;border:2px solid var(--white);background:#d9cfc8}
.quote{left:193px;top:84px;width:440px;font-size:8px;line-height:17px;color:var(--white)}
.quote-mark{font-family:Georgia,serif;font-size:18px;line-height:0}
.author{left:528px;top:124px;width:100px;text-align:right;font-size:11px;color:var(--white)}
.dots{left:364px;top:163px;display:flex;gap:6px;align-items:center}
.dots i{width:6px;height:6px;border-radius:50%;background:var(--white);display:block}
.dots i.active{width:10px;height:10px;border:2px solid var(--white);background:transparent}
.footer-note{left:28px;top:1176px;font-size:7px;color:#444}
.social{left:594px;top:1176px;display:flex;gap:15px}
.social i{width:8px;height:8px;border-radius:50%;background:#333;display:block}
</style>
</head>
<body>
<header>
  <div class="abs topbar"></div>
  <p class="abs contact-line" style="left:76px"><span>Email id :</span> info@brightfold.com</p>
  <div class="abs brand"><div class="brand-dot"></div><div class="brand-name">Brightfold</div></div>
  <p class="abs contact-line" style="left:508px"><span>Call Us :</span> 123-456-7890</p>
  <nav class="abs main-nav"><ul><li>HOME</li><li>FOUNDER</li><li>CONSULTANCY</li><li>SYSTEM</li><li>CASE STUDIES</li><li>CONTACT US</li></ul></nav>
</header>

<section class="abs hero" role="img" aria-label="Photo of business people working at a laptop">
  <div class="abs hero-shade"></div>
  <h1 class="abs hero-title" style="font-weight:400">Brightfold Consultancy<br>Limited Capitalizes</h1>
  <p class="abs hero-text">Lorem ipsum dolor sit amet, consectetur adipiscing elit, sed do eiusmod tempor incididunt ut labore et dolore magna aliqua. Ut enim ad minim veniam, quis nostrud exercitation ullamco laboris nisi ut aliquip ex ea commodo consequat.</p>
  <a class="abs btn hero-btn">READ MORE</a>
  <svg class="abs slider-arrows" viewBox="0 0 39 18"><path d="M15 5l-4 4 4 4M24 5l4 4-4 4" stroke="#222" stroke-width="1.4" fill="none"/></svg>
</section>

<section class="abs welcome">
  <h2 class="abs sec-head" style="top:30px"><span class="sec-dot"></span><span><span class="c-navy">Welcome to </span><span class="c-maroon">Brightfold</span></span></h2>
  <p class="abs welcome-text">Marlow Hayes Contracting provide Project Management &amp; Interior fit-out services to all types of commercial &amp; retail clients. With over 25 years of industry experience, our attention to detail, focus on quality &amp; competitive pricing, ensures repeat business and continued growth with existing clients. If you would like any further information regarding the services that we provide, please do not hesitate to contact us</p>
  <a class="abs btn welcome-btn">READ MORE</a>
</section>

<section class="case-study">
  <h2 class="abs sec-head" style="top:647px"><span class="sec-dot"></span><span><span class="c-navy">Case </span><span class="c-maroon">Study</span></span></h2>
  <svg class="abs" style="left:0;top:693px" width="729" height="216" viewBox="0 0 729 216" font-family="Open Sans, sans-serif" font-weight="600" fill="#fff" text-anchor="middle">
    <defs>
      <linearGradient id="gearTone" x1="0" y1="0" x2="0" y2="1"><stop offset="0" stop-color="#2f4a60"/><stop offset="1" stop-color="#8a7a4a"/></linearGradient>
      <linearGradient id="chartTone" x1="0" y1="0" x2="1" y2="1"><stop offset="0" stop-color="#f2f2f2"/><stop offset="1" stop-color="#9cc4e4"/></linearGradient>
      <linearGradient id="keysTone" x1="0" y1="0" x2="1" y2="1"><stop offset="0" stop-color="#f4f4f4"/><stop offset="1" stop-color="#5a5a5a"/></linearGradient>
    </defs>
    <polygon points="70,0 272,0 232,214 28,214" fill="url(#gearTone)" stroke="#2e3f66" role="img" aria-label="Photo of metal gears and a compass"/>
    <polygon points="284,0 486,0 446,214 244,214" fill="url(#chartTone)" stroke="#2e3f66" role="img" aria-label="Photo of a man beside a rising bar chart arrow"/>
    <polygon points="498,0 699,0 658,214 456,214" fill="url(#keysTone)" stroke="#2e3f66" role="img" aria-label="Photo of hands typing on a laptop"/>
    <polygon points="61,153 247,153 239,195 33,195" fill="var(--navy-band)"/>
    <polygon points="275,153 461,153 453,195 249,195" fill="var(--navy-band)"/>
    <polygon points="489,153 675,153 667,195 463,195" fill="var(--navy-band)"/>
    <text x="138" y="168" font-size="10">Export Credit Agency backed</text>
    <text x="138" y="181" font-size="10">long term Project financing</text>
    <text x="352" y="168" font-size="10">Introducing Regional/Local banks</text>
    <text x="348" y="181" font-size="10">for International Subsidiary Banking</text>
    <text x="565" y="177" font-size="10">Structured Financing</text>
    <g stroke="#fff" stroke-width="1.2">
      <circle cx="133" cy="196" r="9" fill="var(--navy)"/><path d="M131 192l4 4-4 4" fill="none" stroke-width="1.8"/>
      <circle cx="348" cy="196" r="9" fill="var(--navy)"/><path d="M346 192l4 4-4 4" fill="none" stroke-width="1.8"/>
      <circle cx="561" cy="196" r="9" fill="var(--navy)"/><path d="M559 192l4 4-4 4" fill="none" stroke-width="1.8"/>
    </g>
  </svg>
</section>

<section class="abs testimonials">
  <h2 class="abs sec-head" style="top:30px;color:#fff"><span class="sec-dot" style="background:#8fb3d6"></span><span>Client Testimonials</span></h2>
  <div class="abs avatar" role="img" aria-label="Client portrait"></div>
  <p class="abs quote"><span class="quote-mark">“</span>Lorem ipsum dolor sit amet, consectetur adipiscing elit, sed do eiusmod tempor incididunt ut labore et dolore magna aliqua. Ut enim ad minim veniam, quis nostrud exercitation ullamco laboris.<span class="quote-mark">”</span></p>
  <p class="abs author">- Daniel Reeve</p>
  <div class="abs dots"><i></i><i class="active"></i><i></i></div>
</section>

<footer>
  <p class="abs footer-note">All Rights Reserved. Copyrights @company Name. 2016</p>
  <div class="abs social"><i></i><i></i><i></i><i></i><i></i></div>
</footer>
</body>
</html>
```